Business card design needed

Black on pure white.
Two coloured logos.
Text/info on back

Industry/Entity Type

Business

Contact Information for Business Card

Swiftgate Portals Pty. Ltd.
Varnel Corvista High Speed Doors.
Gordon T. Halloway
0491 538260
sales@swiftgateportals.com.au
www.swiftgateportals.com.au

Logo styles of interest
Abstract Logo

```html
<!DOCTYPE html>
<html lang="en">
<head>
<meta charset="utf-8">
<title>Swiftgate Portals – Business Card</title>
<link rel="stylesheet" href="https://fonts.googleapis.com/css2?family=Francois+One&family=Didact+Gothic&display=swap">
<style>
  :root {
    --page: #e9e7e4;
    --card: #ffffff;
    --ink: #111111;
    --heading: #3a3a3a;
    --muted: #6d6d6d;
    --rule: #1a1a1a;
    --brand-green: #3fae49;
  }
  * { box-sizing: border-box; margin: 0; padding: 0; }
  html, body {
    width: 1200px; height: 1000px; overflow: hidden;
    background: var(--page);
  }
  .canvas {
    width: 1200px; height: 1000px;
    display: flex; flex-direction: column; align-items: center; justify-content: center;
    gap: 60px;
  }
  .card {
    position: relative;
    width: 700px; height: 400px;
    background: var(--card);
    box-shadow: 0 4px 18px rgba(0,0,0,0.12);
  }
  .card__rule {
    position: absolute; left: 26px; right: 26px; height: 1.5px;
    background: var(--rule);
  }
  .card__rule--top { top: 30px; }
  .card__rule--bottom { bottom: 30px; }

  /* Front */
  .brand {
    position: absolute; inset: 0;
    display: flex; flex-direction: column; align-items: center; justify-content: center;
    gap: 16px;
  }
  .brand__dot {
    width: 70px; height: 70px; border-radius: 50%;
    background: var(--brand-green);
  }
  .brand__name {
    font-family: "Francois One", sans-serif;
    font-size: 44px; line-height: 1; letter-spacing: 1px;
    color: var(--heading);
    text-transform: uppercase;
  }

  /* Back */
  .company {
    position: absolute; left: 44px; top: 70px;
  }
  .company__name {
    font-family: "Francois One", sans-serif;
    font-size: 30px; color: var(--heading); letter-spacing: 0.3px;
  }
  .company__tagline {
    font-family: "Didact Gothic", sans-serif;
    font-size: 15px; color: var(--muted); letter-spacing: 0.6px;
    margin-top: 2px;
  }
  .contact {
    position: absolute; right: 40px; top: 175px;
    font-family: "Didact Gothic", sans-serif;
    color: var(--ink);
  }
  .contact__person {
    font-family: "Francois One", sans-serif;
    font-size: 19px; color: var(--heading); letter-spacing: 0.3px;
    margin-bottom: 34px;
  }
  .contact__list { list-style: none; }
  .contact__item {
    display: flex; align-items: center; gap: 6px;
    font-size: 14px; line-height: 21px;
  }
  .contact__icon { width: 12px; height: 12px; flex: none; }
</style>
</head>
<body>
<main class="canvas">
  <section class="card card--front" aria-label="Card front">
    <span class="card__rule card__rule--top"></span>
    <div class="brand">
      <span class="brand__dot"></span>
      <span class="brand__name">Swiftgate Portals</span>
    </div>
    <span class="card__rule card__rule--bottom"></span>
  </section>

  <section class="card card--back" aria-label="Card back">
    <span class="card__rule card__rule--top"></span>
    <div class="company">
      <h1 class="company__name">Swiftgate Portals Pty. Ltd.</h1>
      <p class="company__tagline">Varnel Corvista High Speed Doors</p>
    </div>
    <div class="contact">
      <p class="contact__person">Gordon T. Halloway</p>
      <ul class="contact__list">
        <li class="contact__item">
          <svg class="contact__icon" viewBox="0 0 12 12"><path d="M3 1 L5 3.5 L4 5 Q5.5 7.5 7 8 L8.5 7 L11 9 L9.5 11 Q4 10.5 1 3 Z" fill="none" stroke="#111" stroke-width="1"/></svg>
          <span>:&nbsp; 0491 538260</span>
        </li>
        <li class="contact__item">
          <svg class="contact__icon" viewBox="0 0 12 12"><circle cx="6" cy="6" r="2" fill="none" stroke="#111" stroke-width="1.2"/><path d="M8 6 V7.5 Q8 9 9.5 8.5 Q11 7.5 10.8 5.5 A4.8 4.8 0 1 0 8.5 10.2" fill="none" stroke="#111" stroke-width="1.2"/></svg>
          <span>:&nbsp; sales@swiftgateportals.com.au</span>
        </li>
        <li class="contact__item">
          <svg class="contact__icon" viewBox="0 0 12 12"><path d="M2 1 H7.5 L10 3.5 V11 H2 Z" fill="#111"/><path d="M3.5 5.5 H8.5 M3.5 7.5 H8.5 M3.5 9.5 H7" stroke="#fff" stroke-width="0.8"/></svg>
          <span>:&nbsp; www.swiftgateportals.com.au</span>
        </li>
      </ul>
    </div>
    <span class="card__rule card__rule--bottom"></span>
  </section>
</main>
</body>
</html>
```